Commercial Cleaning Company specializing in windows and floors

Looking to have a brochure made for commercial cleaning company. Services include 2 categories:
1. Window Washing

2. Floor Cleaning and Restoration.

Within floor and cleaning restoration, there are several categories:
Carpet Cleaning & Restoration
-Tile and Grout Cleaning & Restoration
-Concrete Cleaning & Restoration
-Stone Cleaning & Restoration (Terrazzo, Marble, Limestone)
-VCT Cleaning & Restoration
-Wood Floor Cleaning & Restoration
-Epoxy Floor Cleaning & Restoration
Floor cleaning Text:
FLOOR CARE:

CARPET FLOORS
Low Moisture, Safe & Fast <--- Increase Font and color
Designed to support a healthy indoor environment, our carpet cleaning methods will eliminate the most common problems caused by other cleaning methods that lead to mold growth, mildew, volatile organic compounds (VOC), insufficient drying times, recurring stains and safety hazards. We also mitigate common safety hazards associated with multiple lengthy hoses, insecure open doors, and slippery hard surfaces. You'll find our system also eliminates both noise and emission pollution around your facility during cleaning times that are common with other cleaning methods.
Our low-moisture system supports a healthy indoor environment so carpets will stay clean & vibrant in color. With superior drying times, our methods eliminates mold growth and mildew. When we are finished cleaning, all that’s left are incredibly clean and fresh smelling carpets

TILE & GROUT FLOORS
We get deep into our cleaning <--- Increase Font and color
Tile and Grout floors can be very difficult to maintain. Often, dirt and grime get trapped in grout lines and crevices and discolor them, making the floors appear dirty. Our company has done all the experimenting for you, and we know the correct brushes, weight kits, machines, and chemical combinations to use to restore and maintain these types of floors, without leaving residue behind that will cause soil to return.

CONCRETE FLOORS
Pores & Crevices are no match <--- Increase Font and color
When it comes to scrubbing and cleaning concrete surfaces such as school hallways, patios, and other types of high traffic concrete flooring, we have you covered.
We're here to keep your employees and visitors safer. We eliminate having to use harsh chemicals and abundances of water to remove the heavy soil that has settled deep down in the concrete pores and crevices.

STONE FLOORS - TERRAZZO, MARBLE, LIMESTONE
We are experts in protecting your major flooring investment. <--- Increase Font and color
If you have high end stone floors, make sure they are performing their best for your facility. We can make educated recommendations on restoration schedules, cleaning methods, schedules, matting and everything related to making your floors "pop". These multi-step processes can be complex, but our experience ensures the best result for your building.

WOOD FLOORS
Wood floors can be tricky - We know how to clean and refinish them. <--- Increase Font and color
If you aren't careful, you may end up with undesirable results when dealing with wood floors. Traditional swing machines can leave swirls if not used correctly, and other methods may damage the wood. We've trained with leading wood floor companies to ensure a process that's safe for your floors and bring you the results you're looking for.

EPOXY FLOORS
We Clean Terrazzo, Flake coating, Screeds & More <--- Increase Font and color

Epoxy is protected from chemicals, dirt, liquids and other contaminants, however, Epoxy floors need to be cleaned routinely as they lose their original luster. We can restore any type of Epoxy floor and bring them back to life.

VCT/VINYL FLOORS <--- Increase Font and color

The most common floor types are our specialty
We can assist you in the maintenance of VCT and vinyl floors. We are helpful resources for assistance with stripping and re coating, daily maintenance, burnishing, and restorative buffing. We have worked with major pad manufacturers and chemical companies to help make selections on the best possible floor maintenance system for these common floors.

Window cleaning Text:
WINDOW CARE:
Our goal is to leave your employees and visitors with the best possible impression of your facility, and clean windows are a huge part of that. BrightHaven uses the latest pure water technology and equipment to leave your windows sparkling clean. We are trained to identify the correct process for various interior and exterior windows, as well as performing restorative processes for things like hard water deposits.
Older cleaning methods often leave behind streaking or residues. BrightHave has invested in equipment that utilizes de-ionized water, microfibers, and state of the art filtration. Recent designs in pole construction allow us to access hard to reach windows, facades, solar panels, sills, and ledges without the use of heavy equipment.
We offer a spate of maintenance programs the ensure the lowest total cost of cleaning. Inquire with us to learn more about why contracting these important cleaning tasks to Brighthaven will relieve you of: equipment storage and maintenance , brush selection, filtration concerns - as well as the liability of work that can sometimes present danger to untrained employees.

Company Biography Page:

BrightHaven is a family based company located in the greater Houston area that specializes in commercial floor care and window cleaning. Our mission is to prioritize the health and safety of the people who use your building by offering cleaning methods that are safe and use the latest industry technology. We understand that a clean, well maintained building has a direct relationship with your image - and that can have a direct effect on your bottom line or reputation. Please consider us for further consultation if you are interested in a no obligation discussion about your facility.

The management of BrightHaven has spent their entire professional lives in the commercial cleaning industry. We have recently sold facility supply distribution company and understand the facility maintenance industry top to bottom. In that time, we've met with innumerable manufacturers, distributors, trade groups, trainers and end users to gain insight into national and regional cleaning trends and methods. We understand budgets, compliance requirements, workflow timelines, and restorative schedules that you don't typically find in a contract cleaning company.
We are confident you will benefit from our wide range of experience and expertise when it comes to maintaining your facility.

Layout:

I think it would work best to have a 4 page single fold booklet type brochure - but open to any suggestions.
The inside would have the 2 services - one side hard floors and the other side windows. Either the front or the back would have our biography on it (probably the back?).
I will give you more input like the address and phone number at the end, it can be added easily.

For the pictures I've added:
The ones that include the word "example" are to be used when incorporating the services.

I've also included a bunch of window pictures. You can use some or none of these (and get other ones) in companion with the text about window cleaning.

Target Market(s)

Commercial buildings and institutions looking for our specific cleaning services

Industry/Entity Type

Commercial Cleaning

Font styles to use
Serif
Sans Serif

Colors
0054AA
0677BA
7BADD7
CADEEF
E8F1F8
0094D4
00A9DD
6FCCEA
C7EBF8
E9F6FB
59FF00
82FF00
B8FF75
E3FFCB
F4FFEA

Requirements
Must have
• All of the included text (can be edited slightly)
Nice to have
• Additional images or text gleened from other sources or past experience that help communicate our business

```html
<!DOCTYPE html>
<html lang="en">
<head>
<meta charset="utf-8">
<title>BrightHaven Brochure</title>
<link rel="stylesheet" href="https://fonts.googleapis.com/css2?family=Montserrat:ital,wght@0,400;0,500;0,600;0,700;0,800;1,600;1,700&display=swap">
<style>
  :root {
    --blue-deep: #0054AA;
    --blue: #0677BA;
    --sky: #0094D4;
    --cyan: #00A9DD;
    --blue-soft: #7BADD7;
    --blue-light: #CADEEF;
    --blue-pale: #E8F1F8;
    --cyan-pale: #E9F6FB;
    --green: #6CC04A;
    --green-light: #8BD35F;
    --gold: #F2B705;
    --ink: #4a4a4a;
    --ink-strong: #333;
    --backdrop: #e4e4e4;
  }
  * { box-sizing: border-box; margin: 0; padding: 0; }
  html, body { width: 1105px; height: 1200px; overflow: hidden; }
  body {
    background: var(--backdrop);
    font-family: "Montserrat", sans-serif;
    color: var(--ink);
    position: relative;
  }
  .page, .spread {
    position: absolute;
    overflow: hidden;
    background: #fff;
  }
  .page { width: 348px; height: 491px; top: 68px; }
  .page--back { left: 217px; background: linear-gradient(180deg, var(--blue-pale) 0%, #f4f8fc 60%, #fff 100%); }
  .page--front { left: 582px; background: #f5f7fa; }
  .spread { left: 217px; top: 596px; width: 710px; height: 491px; }

  .deco { position: absolute; inset: 0; width: 100%; height: 100%; }

  .brand { position: absolute; display: flex; align-items: center; gap: 5px; white-space: nowrap; z-index: 2; }
  .brand-dot { border-radius: 50%; background: var(--sky); flex: none; }
  .brand-name { font-weight: 700; color: var(--blue); font-family: "Montserrat", sans-serif; }

  /* back cover */
  .back-brand { left: 50%; top: 34px; transform: translateX(-50%); }
  .back-brand .brand-dot { width: 12px; height: 12px; }
  .back-brand .brand-name { font-size: 13px; }
  .about-panel {
    position: absolute; left: 22px; top: 66px; width: 296px; height: 308px;
    border-radius: 12px; background: rgba(202, 222, 239, 0.55);
  }
  .about-title {
    position: absolute; left: 0; right: 0; top: 79px; text-align: center;
    font-size: 17px; font-weight: 800; color: var(--blue); letter-spacing: 0.5px;
  }
  .about-copy {
    position: absolute; left: 57px; top: 108px; width: 230px;
    font-size: 7.3px; line-height: 9.05px; color: var(--ink);
  }
  .about-copy p + p { margin-top: 9px; }
  .about-copy p.tight { margin-top: 0; }
  .info {
    position: absolute; left: 0; right: 0; top: 407px; text-align: center; color: #fff;
  }
  .info-label { font-size: 12px; font-weight: 700; color: var(--gold); letter-spacing: 2px; }
  .info-line { font-size: 12px; font-weight: 500; letter-spacing: 1.2px; margin-top: 6px; }

  /* front cover */
  .front-brand { left: 50%; top: 30px; transform: translateX(-50%); }
  .front-brand .brand-dot { width: 20px; height: 20px; }
  .front-brand .brand-name { font-size: 24px; }
  .motto {
    position: absolute; left: 0; right: 0; top: 380px; text-align: center;
  }
  .motto-title { font-size: 13px; font-weight: 700; color: var(--gold); letter-spacing: 0.6px; }
  .motto-copy { font-size: 8.6px; line-height: 10.4px; color: #fff; margin: 5px auto 0; width: 240px; }

  /* inside spread */
  .service-photo { position: absolute; }
  .service-band {
    position: absolute; height: 49px; background: var(--green);
    color: #fff; font-weight: 800; font-size: 16px; line-height: 17.5px;
    text-align: center; display: flex; align-items: center; justify-content: center;
    letter-spacing: 0.5px;
  }
  .window-photo { left: 22px; top: 12px; width: 172px; height: 115px;
    background: linear-gradient(150deg, #8a6a55 0%, #4d6f96 35%, #9ec3e6 60%, #3a5f8c 100%); }
  .window-band { left: 22px; top: 127px; width: 172px; }
  .window-copy {
    position: absolute; left: 22px; top: 176px; width: 172px; height: 307px;
    border: 1px solid var(--green); border-top: none; background: #fff;
    padding: 8px 7px 0 8px; font-size: 7px; line-height: 8.85px;
  }
  .floor-photo { left: 213px; top: 0; width: 142px; height: 127px;
    background: linear-gradient(180deg, #dfe6ea 0%, #b9c3c8 30%, #5a5f63 45%, #3e4246 100%); }
  .floor-band { left: 213px; top: 127px; width: 142px; }
  .floor-copy { position: absolute; left: 215px; top: 188px; width: 140px; font-size: 7px; line-height: 8.85px; }

  .col { position: absolute; font-size: 7px; line-height: 8.85px; }
  .col--one { left: 376px; top: 24px; width: 140px; }
  .col--two { left: 547px; top: 22px; width: 138px; }
  .col-shade { position: absolute; left: 529px; top: 0; width: 170px; height: 491px;
    background: linear-gradient(180deg, var(--blue-light) 0%, var(--blue-pale) 60%, #fff 100%); }

  .floor-type + .floor-type { margin-top: 13px; }
  .floor-type h3 {
    font-size: 12px; line-height: 12.5px; font-weight: 800; color: var(--sky);
  }
  .floor-type .lead {
    font-size: 7.3px; line-height: 8.7px; font-style: italic; font-weight: 700; color: var(--ink-strong);
  }
  .spread-brand { left: 556px; top: 426px; }
  .spread-brand .brand-dot { width: 11px; height: 11px; }
  .spread-brand .brand-name { font-size: 11px; }
</style>
</head>
<body>

<!-- Back cover: About -->
<section class="page page--back" aria-label="Back cover">
  <svg class="deco" viewBox="0 0 348 491" aria-hidden="true">
    <polygon points="0,370 348,330 348,491 0,491" fill="#CADEEF" opacity="0.7"/>
    <polygon points="0,382 348,382 348,491 0,491" fill="#1b8fd8"/>
    <polygon points="0,382 100,382 70,400 0,400" fill="#CADEEF"/>
    <polygon points="200,382 348,360 348,382" fill="#0677BA"/>
    <polygon points="220,410 348,390 348,420 210,430" fill="#0677BA" opacity="0.5"/>
    <polygon points="0,355 100,350 85,370 0,372" fill="#7BADD7" opacity="0.6"/>
  </svg>
  <div class="brand back-brand"><span class="brand-dot"></span><span class="brand-name">BrightHaven</span></div>
  <div class="about-panel"></div>
  <h2 class="about-title">ABOUT US</h2>
  <div class="about-copy">
    <p>BrightHaven is a family based company located in the greater Houston area that specializes in commercial floor care and window cleaning. Our mission is to prioritize the health and safety of the people who use your building by offering cleaning methods that are safe and use the latest industry technology. We understand that a clean, well maintained building has a direct relationship with your image - and that can have a direct effect on your bottom line or reputation. Please consider us for further consultation if you are interested in a no obligation discussion about your facility.</p>
    <p>The management of BrightHaven has spent their entire professional lives in the commercial cleaning industry. We have recently sold facility supply distribution company and understand the facility maintenance industry top to bottom. In that time, we've met with innumerable manufacturers, distributors, trade groups, trainers and end users to gain insight into national and regional cleaning trends and methods. We understand budgets, compliance requirements, workflow timelines, and restorative schedules that you don't typically find in a contract cleaning company.</p>
    <p class="tight">We are confident you will benefit from our wide range of experience and expertise when it comes to maintaining your facility.</p>
  </div>
  <div class="info">
    <div class="info-label">INFORMATION :</div>
    <div class="info-line">www.brighthaven-care.com</div>
    <div class="info-line">+01 555 0142</div>
  </div>
</section>

<!-- Front cover -->
<section class="page page--front" aria-label="Front cover">
  <svg class="deco" viewBox="0 0 348 491">
    <defs>
      <linearGradient id="gClass" x1="0" y1="0" x2="1" y2="1"><stop offset="0" stop-color="#d9d2c8"/><stop offset="1" stop-color="#9a2b2b"/></linearGradient>
      <linearGradient id="gHall" x1="0" y1="0" x2="0" y2="1"><stop offset="0" stop-color="#e7ecef"/><stop offset="1" stop-color="#6f7478"/></linearGradient>
      <linearGradient id="gGlass" x1="0" y1="0" x2="1" y2="1"><stop offset="0" stop-color="#7fb0dd"/><stop offset="1" stop-color="#1d3f6e"/></linearGradient>
      <linearGradient id="gCarpet" x1="0" y1="0" x2="0" y2="1"><stop offset="0" stop-color="#c9d0cf"/><stop offset="1" stop-color="#4a4d50"/></linearGradient>
      <linearGradient id="gTower" x1="0" y1="0" x2="1" y2="1"><stop offset="0" stop-color="#b6d4ee"/><stop offset="1" stop-color="#15335e"/></linearGradient>
      <linearGradient id="gRest" x1="0" y1="0" x2="1" y2="0"><stop offset="0" stop-color="#f0ece6"/><stop offset="1" stop-color="#c8262a"/></linearGradient>
      <linearGradient id="gLobby" x1="0" y1="0" x2="0" y2="1"><stop offset="0" stop-color="#b08a68"/><stop offset="1" stop-color="#b3141c"/></linearGradient>
      <linearGradient id="gLounge" x1="0" y1="0" x2="0" y2="1"><stop offset="0" stop-color="#dfe9ef"/><stop offset="1" stop-color="#c94250"/></linearGradient>
      <linearGradient id="gWood" x1="0" y1="0" x2="0" y2="1"><stop offset="0" stop-color="#f2eeea"/><stop offset="1" stop-color="#a0603a"/></linearGradient>
    </defs>
    <polygon points="0,331 348,331 348,491 0,491" fill="#1b8fd8"/>
    <polygon points="120,331 348,331 348,400 180,400" fill="#0677BA" opacity="0.5"/>
    <polygon points="0,331 60,331 50,350 0,352" fill="#CADEEF"/>
    <polygon points="270,320 348,310 348,331 260,331" fill="#7BADD7"/>
    <g role="img" aria-label="Photo of a classroom with red chairs"><polygon points="0,83 106,83 96,147 0,147" fill="url(#gClass)"/></g>
    <g role="img" aria-label="Photo of a polished airport hallway floor"><polygon points="110,83 228,83 196,147 88,147" fill="url(#gHall)"/></g>
    <g role="img" aria-label="Photo of a squeegee cleaning an office window"><polygon points="232,83 348,83 348,147 200,147" fill="url(#gGlass)"/></g>
    <g role="img" aria-label="Photo of a carpeted office floor"><polygon points="0,151 66,151 60,232 0,232" fill="url(#gCarpet)"/></g>
    <g role="img" aria-label="Photo of a glass office tower"><polygon points="70,151 196,151 148,232 64,232" fill="url(#gTower)"/></g>
    <g role="img" aria-label="Photo of a restroom with red stall doors"><polygon points="200,151 348,151 348,232 152,232" fill="url(#gRest)"/></g>
    <g role="img" aria-label="Photo of a lobby with a red carpet"><polygon points="0,236 116,236 92,314 0,314" fill="url(#gLobby)"/></g>
    <g role="img" aria-label="Photo of an office lounge with red sofas"><polygon points="120,236 240,236 212,314 96,314" fill="url(#gLounge)"/></g>
    <g role="img" aria-label="Photo of an empty room with a wood floor"><polygon points="244,236 348,236 348,314 216,314" fill="url(#gWood)"/></g>
  </svg>
  <div class="brand front-brand"><span class="brand-dot"></span><span class="brand-name">BrightHaven</span></div>
  <div class="motto">
    <div class="motto-title">DIAGNOSTIC &nbsp;-&nbsp; CLEAN &nbsp;-&nbsp; REPAIR</div>
    <p class="motto-copy">We prioritize the health and safety of the people who use your building by offering cleaning methods that are safe and use the latest industry technology</p>
  </div>
</section>

<!-- Inside spread -->
<section class="spread" aria-label="Inside spread">
  <div class="col-shade"></div>
  <svg class="deco" viewBox="0 0 710 491" aria-hidden="true">
    <polygon points="0,0 170,0 10,170 0,180" fill="#0094D4"/>
    <polygon points="0,0 60,0 0,70" fill="#0054AA"/>
    <polygon points="0,230 30,200 22,260 0,280" fill="#CADEEF"/>
    <line x1="355" y1="0" x2="355" y2="491" stroke="#e2e6ea" stroke-width="1"/>
    <polygon points="710,400 710,491 620,491" fill="#0094D4"/>
    <polygon points="710,435 710,491 655,491" fill="#0054AA"/>
    <polygon points="590,491 705,412 708,420 612,491" fill="#7BADD7" opacity="0.8"/>
    <polygon points="700,0 710,0 710,491 700,491" fill="#f2f4f6"/>
  </svg>

  <div class="service-photo window-photo" role="img" aria-label="Photo of a squeegee on a glass building facade"></div>
  <div class="service-band window-band">WINDOW<br>CARE</div>
  <div class="window-copy">
    Our goal is to leave your employees and visitors with the best possible impression of your facility, and clean windows are a huge part of that. BrightHaven uses the latest pure water technology and equipment to leave your windows sparkling clean. We are trained to identify the correct process for various interior and exterior windows, as well as performing restorative processes for things like hard water deposits.<br>
    Older cleaning methods often leave behind streaking or residues. BrightHave has invested in equipment that utilizes de-ionized water, microfibers, and state of the art filtration. Recent designs in pole construction allow us to access hard to reach windows, facades, solar panels, sills, and ledges without the use of heavy equipment.<br>
    We offer a spate of maintenance programs the ensure the lowest total cost of cleaning. Inquire with us to learn more about why contracting these important cleaning tasks to Brighthaven will relieve you of: equipment storage and maintenance , brush selection, filtration concerns - as well as the liability of work that can sometimes present danger to untrained employees.
  </div>

  <div class="service-photo floor-photo" role="img" aria-label="Photo of an office with patterned carpet tiles"></div>
  <div class="service-band floor-band">FLOOR<br>CARE</div>
  <div class="floor-copy">
    <div class="floor-type">
      <h3>Carpet Floors</h3>
      <p class="lead">Low Moisture, Safe &amp; Fast.</p>
      <p>Designed to support a healthy indoor environment, our carpet cleaning methods will eliminate the most common problems caused by other cleaning methods that lead to mold growth, mildew, volatile organic compounds (VOC), insufficient drying times, recurring stains and safety hazards. We also mitigate common safety hazards associated with multiple lengthy hoses, insecure open doors, and slippery hard surfaces. You'll find our system also eliminates both noise and emission pollution around your facility during cleaning times that are common with other cleaning methods.<br>Our low-moisture system supports a healthy indoor environment so carpets will stay clean &amp; vibrant in color. With superior drying times, our methods eliminates mold growth and mildew. When we are finished cleaning, all that's left are incredibly clean and fresh smelling carpets</p>
    </div>
  </div>

  <div class="col col--one">
    <div class="floor-type">
      <h3>Tile &amp; Grout Floors</h3>
      <p class="lead">We get deep into our cleaning.</p>
      <p>Tile and Grout floors can be very difficult to maintain. Often, dirt and grime get trapped in grout lines and crevices and discolor them, making the floors appear dirty. Our company has done all the experimenting for you, and we know the correct brushes, weight kits, machines, and chemical combinations to use to restore and maintain these types of floors, without leaving residue behind that will cause soil to return.</p>
    </div>
    <div class="floor-type">
      <h3>Concrete Floors</h3>
      <p class="lead">Pores &amp; Crevices are no match.</p>
      <p>When it comes to scrubbing and cleaning concrete surfaces such as school hallways, patios, and other types of high traffic concrete flooring, we have you covered.<br>We're here to keep your employees and visitors safer. We eliminate having to use harsh chemicals and abundances of water to remove the heavy soil that has settled deep down in the concrete pores and crevices.</p>
    </div>
    <div class="floor-type">
      <h3>Stone Floors -<br>Terrazzo, Marble,<br>Limestone</h3>
      <p class="lead">We are experts in protecting your major flooring investment.</p>
      <p>If you have high end stone floors, make sure they are performing their best for your facility. We can make educated recommendations on restoration schedules, cleaning methods, schedules, matting and everything related to making your floors "pop". These multi-step processes can be complex, but our experience ensures the best result for your building.</p>
    </div>
  </div>

  <div class="col col--two">
    <div class="floor-type">
      <h3>Wood Floors</h3>
      <p class="lead">Wood floors can be tricky - We know how to clean and refinish them.</p>
      <p>If you aren't careful, you may end up with undesirable results when dealing with wood floors. Traditional swing machines can leave swirls if not used correctly, and other methods may damage the wood. We've trained with leading wood floor companies to ensure a process that's safe for your floors and bring you the results you're looking for.</p>
    </div>
    <div class="floor-type">
      <h3>Epoxy Floors</h3>
      <p class="lead">We Clean Terrazzo, Flake coating, Screeds &amp; More.</p>
      <p>Epoxy is protected from chemicals, dirt, liquids and other contaminants, however, Epoxy floors need to be cleaned routinely as they lose their original luster. We can restore any type of Epoxy floor and bring them back to life.</p>
    </div>
    <div class="floor-type">
      <h3>Vct/vinyl Floors</h3>
      <p class="lead">The most common floor types are our specialty</p>
      <p>We can assist you in the maintenance of VCT and vinyl floors. We are helpful resources for assistance with stripping and re coating, daily maintenance, burnishing, and restorative buffing. We have worked with major pad manufacturers and chemical companies to help make selections on the best possible floor maintenance system for these common floors.</p>
    </div>
  </div>

  <div class="brand spread-brand"><span class="brand-dot"></span><span class="brand-name">BrightHaven</span></div>
</section>

</body>
</html>
```